Redesign of an insurance website

Attached is an insurance website that I need to redesign. Currently the website is too dark. I like for example www.brambleshield.com . Could you make the website lighter and change the structure a little so that it is more user friendly?

Industry/Entity Type

Insurance

Number of Pages Required

4 page

```html
<!DOCTYPE html>
<html lang="cs">
<head>
<meta charset="utf-8">
<title>Jistota24.cz – srovnání pojištění</title>
<link rel="stylesheet" href="https://fonts.googleapis.com/css2?family=Noto+Serif:wght@700&family=Open+Sans:wght@400;600&family=Ubuntu:wght@300;400&display=swap">
<style>
  :root {
    --blue: #3d8af7;
    --orange: #f26522;
    --orange-soft: #f5803e;
    --dark-grey: #5b5b5b;
    --ink: #1d1d1d;
    --text: #666666;
    --line: #cfcfcf;
    --white: #ffffff;
  }
  * { box-sizing: border-box; margin: 0; padding: 0; }
  html, body { width: 1196px; height: 1200px; overflow: hidden; background: var(--white); }
  body { position: relative; font-family: "Ubuntu", sans-serif; color: var(--ink); }

  .top-rule { position: absolute; left: 0; top: 0; width: 1196px; height: 3px; background: var(--orange); }

  .brand { position: absolute; left: 98px; top: 28px; font-family: "Noto Serif", serif; font-weight: 700; font-size: 29px; color: var(--blue); letter-spacing: -0.3px; }

  .main-nav a { position: absolute; top: 38px; font-family: "Open Sans", sans-serif; font-weight: 600; font-size: 15px; color: var(--dark-grey); text-decoration: none; }
  .nav-btn { position: absolute; top: 31px; height: 32px; line-height: 32px; text-align: center; font-family: "Open Sans", sans-serif; font-weight: 600; font-size: 14px; color: var(--white); text-decoration: none; border-radius: 2px; }
  .nav-btn.login { left: 835px; width: 120px; background: var(--orange-soft); }
  .nav-btn.register { left: 973px; width: 123px; background: var(--dark-grey); }

  .hero { position: absolute; left: 0; top: 101px; width: 1196px; height: 538px;
    background: linear-gradient(90deg, #6f7a3a 0%, #a89a56 22%, #d8cfa0 42%, #f1ecd8 56%, #efe9d2 75%, #e8e4cc 100%); }
  .hero-fade { position: absolute; right: 0; top: 0; width: 700px; height: 538px;
    background: radial-gradient(ellipse at 55% 40%, rgba(255,255,250,0.75), rgba(255,255,250,0) 70%); }

  .hero-title { position: absolute; right: 100px; top: 176px; font-family: "Noto Serif", serif; font-weight: 700; font-size: 20px; color: var(--ink); }

  .carousel { position: absolute; left: 620px; top: 236px; }
  .product-label { position: absolute; left: 648px; width: 360px; top: 385px; text-align: center; font-family: "Noto Serif", serif; font-weight: 700; font-size: 14.5px; }

  .field { position: absolute; top: 432px; width: 171px; height: 42px; background: #fafafa; border: 1px solid #d4d4d4; border-radius: 3px; padding-left: 19px; line-height: 40px; font-family: "Ubuntu", sans-serif; font-size: 12.5px; color: #777; }
  .consent { position: absolute; left: 727px; top: 498px; font-size: 12px; color: var(--ink); display: flex; align-items: center; gap: 10px; }
  .consent .box { width: 10px; height: 10px; border: 1.5px solid #333; border-radius: 2px; }

  .btn { position: absolute; background: var(--orange); color: var(--white); font-family: "Noto Serif", serif; font-weight: 700; text-align: center; text-decoration: none; border-radius: 2px; }
  .btn.calc { left: 744px; top: 537px; width: 169px; height: 41px; line-height: 41px; font-size: 15px; }

  .advice-photo { position: absolute; left: 98px; top: 719px; width: 397px; height: 284px; border: 1px solid #e6e6e6; box-shadow: 0 0 3px rgba(0,0,0,0.08); padding: 3px; background: var(--white); }
  .advice-photo div { width: 100%; height: 100%; background: linear-gradient(135deg, #eef1f3 0%, #d9dfe3 40%, #c4d3e4 70%, #e9e6e1 100%); }

  .advice-title { position: absolute; left: 557px; top: 714px; width: 540px; font-family: "Noto Serif", serif; font-weight: 700; font-size: 25.5px; line-height: 37.5px; color: var(--ink); }
  .advice-text { position: absolute; left: 557px; top: 819px; width: 540px; font-size: 12.8px; line-height: 25.6px; color: var(--text); text-align: justify; }
  .btn.save { left: 557px; top: 962px; width: 154px; height: 41px; line-height: 43px; font-size: 15px; }

  .footer-rule { position: absolute; left: 98px; top: 1094px; width: 999px; height: 1px; background: var(--line); }
  .copyright { position: absolute; left: 98px; top: 1140px; font-size: 14.5px; font-weight: 300; color: var(--text); }
  .copyright .sep { margin: 0 16px 0 18px; }
  .social { position: absolute; top: 1129px; width: 40px; height: 40px; border-radius: 50%; }
  .social.s1 { left: 959px; background: #41609e; }
  .social.s2 { left: 1007px; background: #e9472d; }
  .social.s3 { left: 1056px; background: #27a5e8; }
</style>
</head>
<body>
  <div class="top-rule"></div>

  <header>
    <div class="brand">JISTOTA24.CZ</div>
    <nav class="main-nav">
      <a href="#" style="left:511px">O NÁS</a>
      <a href="#" style="left:590px">CASTE DOTAZY</a>
      <a href="#" style="left:736px">KONTAKT</a>
    </nav>
    <a href="#" class="nav-btn login">PRIHLASIT SE</a>
    <a href="#" class="nav-btn register">REGISTROVAT</a>
  </header>

  <section class="hero" role="img" aria-label="Rodina procházející se po louce u řeky při západu slunce">
    <div class="hero-fade"></div>
  </section>

  <h1 class="hero-title">PROČ HLEDAT POJIŠTĚNÍ PŘES JISTOTA24.CZ?</h1>

  <svg class="carousel" width="420" height="140" viewBox="0 0 420 140" aria-label="Výběr typu pojištění">
    <polyline points="24,55 16,65 24,75" fill="none" stroke="#555" stroke-width="2.5"/>
    <polyline points="392,55 400,65 392,75" fill="none" stroke="#555" stroke-width="2.5"/>
    <circle cx="119" cy="65" r="43" fill="none" stroke="#3d8af7" stroke-width="2"/>
    <circle cx="298" cy="65" r="43" fill="none" stroke="#3d8af7" stroke-width="2"/>
    <!-- plane -->
    <g fill="#3d8af7" transform="translate(119,65) rotate(-20)">
      <path d="M-26,-3 L22,-3 Q30,0 22,3 L-26,3 Z"/>
      <path d="M-2,-3 L-14,-20 L-7,-20 L10,-3 Z"/>
      <path d="M-2,3 L-14,20 L-7,20 L10,3 Z"/>
      <path d="M-24,-3 L-28,-12 L-22,-12 L-16,-3 Z"/>
    </g>
    <!-- house -->
    <g fill="#3d8af7">
      <path d="M298,47 L318,65 L313,65 L298,52 L283,65 L278,65 Z"/>
      <path d="M286,64 L298,54 L310,64 L310,80 L302,80 L302,70 L294,70 L294,80 L286,80 Z"/>
    </g>
    <circle cx="208" cy="65" r="58" fill="#3d8af7"/>
    <!-- car -->
    <g fill="#ffffff" transform="translate(208,65) rotate(-22)">
      <path d="M-32,-2 L-26,-12 L-12,-13 L-4,-22 L16,-22 L26,-12 L32,-10 L32,2 Z"/>
      <circle cx="-18" cy="4" r="7" fill="#3d8af7" stroke="#fff" stroke-width="3"/>
      <circle cx="20" cy="4" r="7" fill="#3d8af7" stroke="#fff" stroke-width="3"/>
    </g>
  </svg>

  <div class="product-label">HAVARIJNI POJISTENI</div>

  <form>
    <div class="field" style="left:562px">Jméno</div>
    <div class="field" style="left:744px">Příjmení</div>
    <div class="field" style="left:926px">E-mail</div>
    <label class="consent"><span class="box"></span>Souhlasím s podmínkami použití</label>
    <a href="#" class="btn calc">SPOČÍTAT CENU</a>
  </form>

  <section>
    <figure class="advice-photo"><div role="img" aria-label="Poradkyně vysvětluje pojistnou smlouvu staršímu páru"></div></figure>
    <h2 class="advice-title">UZAVŘELI JSTE V MINULOSTI NEVÝHODNOU POJISTKU? ZBAVTE SE JÍ!</h2>
    <p class="advice-text">Máte pocit, že za stávající pojištění platíte příliš? A že za své peníze dostáváte méně služeb než druzí? Pojďte s tím něco udělat! S námi najdete tu nejvýhodnější nabídku na trhu a navíc vám poradíme, jak se nejsnáze zbavit starého nevýhodného pojištění. Stačí kliknout na tlačítko UŠETŘIT a můžete se vydat na cestu k lepšímu a levnějšímu pojištění.</p>
    <a href="#" class="btn save">CHCI UŠETŘIT</a>
  </section>

  <footer>
    <div class="footer-rule"></div>
    <div class="copyright">© Copyright 2017 Jistota24.cz. All Rights Reserved<span class="sep">|</span>Privacy Policy</div>
    <a href="#" class="social s1" aria-label="Sociální síť"></a>
    <a href="#" class="social s2" aria-label="Sociální síť"></a>
    <a href="#" class="social s3" aria-label="Sociální síť"></a>
  </footer>
</body>
</html>
```